Need Eye Catching For Sale By Owner Signs

In need of a Eye Catching For Sale By Owner Sign design. I plan on using the sign to market buildings and raw land that I own. The design should be able to scale to different rectangular dimensions for example a yard stake sign or a large 4' x 6' sign to be tacked to plywood. The design should have a dead space near the bottom that I can insert more detail information into at a later time.

The main tag line "For Sale By Owner" and the contact number "318-562-4097" needs to be easily be read from a distance.

```html
<!DOCTYPE html>
<html lang="en">
<head>
<meta charset="utf-8">
<title>For Sale By Owner Sign</title>
<link href="https://fonts.googleapis.com/css2?family=Jost:wght@500;600;700&display=swap" rel="stylesheet">
<style>
  :root {
    --bg-light: #fbfbfb;
    --bg-shade: #e4e4e4;
    --ribbon-top: #4eae1c;
    --ribbon-bottom: #2a7a00;
    --ribbon-edge: #6fd43a;
    --tag-text: #ffffff;
    --owner-gray: #666666;
    --phone-red: #e0001b;
    --band-white: #ffffff;
    --frame-red: #d8001a;
  }
  * { margin: 0; padding: 0; box-sizing: border-box; }
  html, body { width: 800px; height: 1200px; overflow: hidden; }
  body {
    font-family: 'Jost', 'Century Gothic', sans-serif;
    background: linear-gradient(90deg, var(--bg-shade) 0%, var(--bg-light) 30%, var(--bg-light) 70%, var(--bg-shade) 100%);
  }
  .sign { position: relative; width: 800px; height: 1200px; overflow: hidden; }
  .hero-disc {
    position: absolute; left: -85px; top: -385px;
    width: 970px; height: 970px; border-radius: 50%;
    background: radial-gradient(circle at 50% 40%, #ffffff 0%, #f6f6f6 60%, #e2e2e2 100%);
    box-shadow: 0 4px 8px rgba(0,0,0,0.08);
  }
  .ribbon { position: absolute; left: 180px; top: 20px; width: 420px; height: 490px; }
  .tag-line {
    position: absolute; left: 185px; width: 408px; text-align: center;
    color: var(--tag-text); font-weight: 600; white-space: nowrap;
    text-shadow: 0 3px 5px rgba(0,0,0,0.25);
  }
  .tag-for { top: 72px; font-size: 80px; line-height: 1; }
  .tag-sale { top: 186px; font-size: 158px; line-height: 1; letter-spacing: -3px; }
  .by-owner {
    position: absolute; top: 490px; left: 0; width: 800px; text-align: center;
    color: var(--owner-gray); font-size: 57px; font-weight: 600; line-height: 1;
    white-space: nowrap;
  }
  .phone-band {
    position: absolute; left: 0; top: 603px; width: 800px; height: 167px;
    background: var(--band-white);
    box-shadow: 0 -3px 6px rgba(0,0,0,0.06), 0 4px 8px rgba(0,0,0,0.1);
    display: flex; align-items: center; justify-content: center;
  }
  .phone-number {
    color: var(--phone-red); font-size: 116px; font-weight: 700;
    line-height: 1; white-space: nowrap;
  }
  .detail-box {
    position: absolute; left: 52px; top: 815px; width: 697px; height: 340px;
    background: #ffffff; border: 2px solid var(--frame-red);
    box-shadow: 2px 4px 6px rgba(0,0,0,0.25);
  }
</style>
</head>
<body>
<div class="sign">
  <div class="hero-disc"></div>
  <svg class="ribbon" viewBox="0 0 420 490" aria-hidden="true">
    <defs>
      <linearGradient id="ribbonFill" x1="0" y1="0" x2="0" y2="1">
        <stop offset="0" stop-color="#4eae1c"/>
        <stop offset="0.6" stop-color="#307f04"/>
        <stop offset="1" stop-color="#2a7a00"/>
      </linearGradient>
      <filter id="ribbonShadow" x="-10%" y="-10%" width="120%" height="130%">
        <feDropShadow dx="0" dy="8" stdDeviation="8" flood-color="#000" flood-opacity="0.25"/>
      </filter>
    </defs>
    <path d="M5 8 H413 V480 L208 385 L5 480 Z" fill="url(#ribbonFill)" filter="url(#ribbonShadow)"/>
    <path d="M5 480 L208 385 L413 480" fill="none" stroke="#6fd43a" stroke-width="2"/>
    <path d="M13 8 V466 M405 8 V466" stroke="#5cbf2a" stroke-width="1" opacity="0.5"/>
  </svg>
  <div class="tag-line tag-for">FOR</div>
  <div class="tag-line tag-sale">SALE</div>
  <div class="by-owner">By Owner</div>
  <div class="phone-band"><span class="phone-number">318-562-4097</span></div>
  <div class="detail-box"></div>
</div>
</body>
</html>
```